Inspiring Poster for Company Staff Room

What we need:
We want an awesome design to create a poster that will be plaque mounted in our staff room. We just went through a very motivating workshop to discover our "WHY" as a company...basically, to define the reason we are in business, and to define what motivates us to come to work every day. The poster must be motivating but really resonate with our team…we are not looking for a “typical” motivational poster that we can purchase off Amazon!

Who we are:
We are a property management company, a team of 20 that is passionate about our investors, and residents who rent from us, but more importantly, we love helping people and making a difference in our industry. We are proud and work hard for every single 5 star Google review we achieve.

Information for you:
We have included a mock up of the poster, which words we want, and the placement of them (in a general sense) but we need a designer to really bring this together in an inspiring poster that represents our company’s culture, feel, and fit. We have also included a logo file, as well as examples of our business cards, letterhead and thank you card already designed.
Here are the parameters:

(1) Poster size: 24” x 36”
(2) Full colour
(3) Must incorporate our company logo
(4) Must incorporate the following words:

Why do I come to work?

“To feel fulfilled by empathizing, educating and empowering our clients and co-workers so that we can build strong, impactful relationships”

Own the outcome

(5) Please see our website at www.brindlecovepm.com to get a feel for our company culture and for a better idea of our current company graphics

Target Market(s)

Our staff. Will not be seen by our clients

Industry/Entity Type

Real Estate

Font styles to use
Serif
Sans Serif

Requirements
Should not have
• Would not want this to be too "busy." if you can picture it, the poster will be mounted on the wall as soon as someone enters the room. The idea is to remind them each day why they come to work.

```html
<!DOCTYPE html>
<html lang="en">
<head>
<meta charset="utf-8">
<title>Why Do I Come To Work – Staff Room Poster</title>
<link rel="stylesheet" href="https://fonts.googleapis.com/css2?family=Orbitron:wght@700;800;900&family=Montserrat:wght@400;500;700&display=swap">
<style>
  :root {
    --blue: #35a3dc;
    --blue-mid: #4aaee2;
    --blue-light: #9bd2ec;
    --charcoal: #484746;
    --ink: #1a1a1a;
    --rule: #8a8a8a;
    --paper: #ffffff;
  }
  * { margin: 0; padding: 0; box-sizing: border-box; }
  html, body { width: 800px; height: 1200px; overflow: hidden; background: var(--paper); }
  .poster { position: relative; width: 800px; height: 1200px; overflow: hidden; background: var(--paper); font-family: "Montserrat", sans-serif; color: var(--ink); }
  .shapes { position: absolute; inset: 0; }
  .display { font-family: "Orbitron", sans-serif; font-weight: 900; }
  .mission {
    position: absolute; left: 73px; top: 425px; width: 660px;
    font-size: 26.4px; line-height: 33.6px; font-weight: 400; letter-spacing: 0.2px;
  }
  .key { position: absolute; left: 463px; width: 260px; }
  .key h2 {
    font-family: "Orbitron", sans-serif; font-weight: 900; color: var(--blue);
    font-size: 15px; letter-spacing: 0.5px; line-height: 18px; margin-bottom: 2px;
    text-transform: uppercase;
  }
  .key h2 .cap { font-size: 21px; }
  .key p { font-size: 13.6px; line-height: 17.4px; font-weight: 500; }
  .key em { font-style: normal; color: var(--blue); }
  .key-what { top: 640px; }
  .key-how { top: 763px; }
  .key-why { top: 886px; }
  .key-rule { position: absolute; left: 463px; width: 259px; height: 1px; background: var(--rule); }
  .brand { position: absolute; left: 463px; top: 1046px; display: flex; align-items: center; gap: 12px; }
  .brand-mark { width: 44px; height: 44px; background: var(--charcoal); }
  .brand-name { font-family: "Montserrat", sans-serif; font-weight: 700; color: var(--blue); text-transform: uppercase; line-height: 1; }
  .brand-name .line-main { display: block; font-size: 25px; letter-spacing: 1px; }
  .brand-name .line-sub { display: block; font-size: 10.5px; letter-spacing: 2.4px; margin-top: 5px; }
</style>
</head>
<body>
<div class="poster">
  <svg class="shapes" width="800" height="1200" viewBox="0 0 800 1200">
    <polygon class="band-top" fill="var(--charcoal)" points="0,0 800,0 800,83 713,83 544,121 375,83 0,83"/>
    <polygon class="band-bottom" fill="var(--blue)" points="0,1117 87,1117 256,1078 426,1117 800,1117 800,1200 0,1200"/>

    <g class="display" fill="var(--blue)">
      <text x="73" y="210" font-size="83" textLength="649" lengthAdjust="spacingAndGlyphs">W<tspan font-size="70">HY DO I</tspan></text>
      <text x="77" y="297" font-size="70" textLength="596" lengthAdjust="spacingAndGlyphs">COME TO</text>
      <text x="73" y="384" font-size="70" textLength="483" lengthAdjust="spacingAndGlyphs">WORK?</text>
    </g>

    <text class="display" x="75" y="588" font-size="37" fill="var(--charcoal)" textLength="644" lengthAdjust="spacingAndGlyphs">O<tspan font-size="32">WN THE OUTCOME</tspan></text>

    <g class="golden-circle">
      <circle cx="255" cy="815" r="183" fill="var(--blue-light)"/>
      <circle cx="255" cy="815" r="131" fill="var(--blue-mid)"/>
      <circle cx="255" cy="815" r="67" fill="var(--blue)"/>
      <g class="display" fill="#ffffff" font-size="28" text-anchor="middle">
        <text x="256" y="828" textLength="114" lengthAdjust="spacingAndGlyphs">WHY</text>
        <text x="256" y="922" textLength="113" lengthAdjust="spacingAndGlyphs">HOW</text>
        <text x="256" y="981" textLength="140" lengthAdjust="spacingAndGlyphs">WHAT</text>
      </g>
    </g>
  </svg>

  <p class="mission">“To feel fulfilled by empathizing, educating and empowering our clients and co-workers so that we can build strong, impactful relationships”</p>

  <section class="key key-what">
    <h2><span class="cap">W</span>hat</h2>
    <p>Every organization on the planet knows <em>WHAT</em> they do. These are products they sell or the services they offer.</p>
  </section>
  <div class="key-rule" style="top:748px"></div>
  <section class="key key-how">
    <h2><span class="cap">H</span>ow</h2>
    <p>Some organisations know <em>HOW</em> they do it. These are the things that make them special or set them apart from their competition.</p>
  </section>
  <div class="key-rule" style="top:871px"></div>
  <section class="key key-why">
    <h2><span class="cap">W</span>hy</h2>
    <p>Very few organisations know <em>WHY</em> they do what they do. WHY is not about making money. That’s a result. It’s a purpose, cause or belief. It’s the very reason your organization exists.</p>
  </section>

  <div class="brand">
    <span class="brand-mark"></span>
    <span class="brand-name"><span class="line-main">Brindle Cove</span><span class="line-sub">Property Management</span></span>
  </div>
</div>
</body>
</html>
```